Sydney law firm, Prestwicks Solicitors, needs a flyer design!

We need a flyer design for our law firm which has been operating in Sydney for over 35 years. We want to send the flyer out to potential clients and also to existing clients to let them know the range of services that we provide. Our corporate colours are white, red and black and we would like these incorporated somewhat. The final design should be clean, modern and professional.

We would like the design to fit a double sided flyer approx. 210mm high x 100mm wide.

Industry/Entity Type

Law Firm

Font styles to use
Serif
Sans Serif

Colors
eb2026
ffffff

Requirements
Must have
• Details needed on the flyer are:
• Prestwicks Solicitors
• 3/82 Carradine Street, Liverpool, NSW 2170
• (02) 9418 3562
• www.prestwickssolicitors-example.com.au
• info@prestwickssolicitors-example.com.au
• Our areas of practice include:
• Property Law
• Conveyancing
• Leases
• Criminal Law
• Family Law
• Litigation and Dispute Resolution
• Company Law
• Wills and Estates
• Powers of Attorney and Guardianship
Should not have
• a picture of scales or a picture of a gavel

```html
<!DOCTYPE html>
<html lang="en">
<head>
<meta charset="utf-8">
<title>Prestwicks Solicitors – Flyer</title>
<link rel="stylesheet" href="https://fonts.googleapis.com/css2?family=Lato:wght@400;700&family=Roboto+Condensed:wght@700&display=swap">
<style>
  :root {
    --red: #eb2026;
    --red-dark: #8e0f14;
    --black: #111111;
    --charcoal: #3a3a3a;
    --white: #ffffff;
    --page: #e6e6e6;
    --ink: #1a1a1a;
  }
  * { margin: 0; padding: 0; box-sizing: border-box; }
  html, body { width: 900px; height: 1200px; overflow: hidden; background: var(--page); }
  .flyer {
    position: absolute; left: 194px; top: 60px; width: 513px; height: 1080px;
    background: var(--white); overflow: hidden;
    box-shadow: 0 4px 18px rgba(0,0,0,.25);
    font-family: "Lato", sans-serif; color: var(--ink);
  }
  .flyer-art { position: absolute; inset: 0; }
  .brand {
    position: absolute; right: 20px; top: 36px; text-align: right;
    font-family: "Lato", sans-serif; font-weight: 700; color: var(--ink);
  }
  .brand-name { font-size: 38px; line-height: 1; letter-spacing: 1px; }
  .brand-sub { font-size: 13px; letter-spacing: 8px; margin-top: 10px; margin-right: -8px; }

  .practice-areas {
    position: absolute; left: 16px; top: 262px; width: 481px;
    background: rgba(17,17,17,.72); border-left: 4px solid var(--red);
    padding: 12px 14px 12px 16px; color: var(--white);
  }
  .practice-title {
    font-family: "Roboto Condensed", sans-serif; font-weight: 700; font-size: 18px;
    line-height: 1; color: var(--white); margin-bottom: 9px;
  }
  .practice-title .accent { color: var(--red); }
  .practice-list {
    list-style: none; columns: 2; column-gap: 14px;
    font-size: 13px; line-height: 19px; font-weight: 700;
  }
  .practice-list li { break-inside: avoid; padding-left: 12px; position: relative; }
  .practice-list li::before {
    content: ""; position: absolute; left: 0; top: 7px; width: 5px; height: 5px; background: var(--red);
  }

  .call-box {
    position: absolute; left: 40px; top: 446px; width: 226px; height: 114px;
    background: linear-gradient(#6a6a6a, #3c3c3c);
    border: 3px solid var(--white); border-radius: 6px 6px 22px 22px;
    box-shadow: 0 3px 8px rgba(0,0,0,.4);
    text-align: center; font-family: "Roboto Condensed", sans-serif; font-weight: 700;
  }
  .call-label { color: var(--red); font-size: 37px; line-height: 1; margin-top: 12px; }
  .call-number { color: var(--white); font-size: 31px; line-height: 1; margin-top: 6px; }
  .section-tag {
    position: absolute; left: 10px; top: 593px; width: 135px; height: 32px;
    background: var(--black); color: var(--white); border-radius: 0 16px 16px 0;
    font-family: "Roboto Condensed", sans-serif; font-weight: 700; font-size: 23px;
    line-height: 32px; padding-left: 8px;
  }
  .about-text {
    position: absolute; left: 16px; top: 638px; width: 468px;
    font-size: 15.5px; line-height: 20px; font-weight: 700; color: var(--ink);
    hyphens: auto;
  }
  .about-text p + p { margin-top: 8px; }
  .promise-banner {
    position: absolute; left: 10px; top: 818px; width: 491px; height: 100px;
    background: linear-gradient(90deg, #5b0a0d, var(--red) 45%, var(--red) 60%, #5b0a0d);
    border: 3px solid #b8b8b8; box-shadow: 0 3px 8px rgba(0,0,0,.35);
    text-align: center; font-family: "Roboto Condensed", sans-serif; font-weight: 700;
    padding-top: 18px;
  }
  .promise-line-1 { font-size: 30px; line-height: 1; color: var(--black); }
  .promise-line-1 .accent { color: var(--white); }
  .promise-line-2 { font-size: 23px; line-height: 1; color: var(--white); margin-top: 6px; }
  .contact-list {
    position: absolute; left: 16px; top: 980px; list-style: none;
    font-family: "Roboto Condensed", sans-serif; font-weight: 700; font-size: 17px; color: var(--white);
  }
  .contact-list li { display: flex; align-items: center; height: 29px; }
  .contact-list svg { width: 17px; height: 17px; margin-right: 14px; fill: var(--red); }
</style>
</head>
<body>
<main class="flyer">
  <svg class="flyer-art" viewBox="0 0 513 1080" width="513" height="1080">
    <defs>
      <linearGradient id="photoTone" x1="0" y1="0" x2="1" y2="1">
        <stop offset="0" stop-color="#1b1b1b"/><stop offset=".45" stop-color="#8a8a8a"/><stop offset="1" stop-color="#1e1e1e"/>
      </linearGradient>
      <linearGradient id="redSweep" x1="0" y1="0" x2="1" y2="0">
        <stop offset="0" stop-color="#1a1a1a"/><stop offset=".5" stop-color="#8e0f14"/><stop offset="1" stop-color="#eb2026"/>
      </linearGradient>
      <linearGradient id="lowerTone" x1="0" y1="0" x2="0" y2="1">
        <stop offset="0" stop-color="#ffffff"/><stop offset=".45" stop-color="#ececec"/><stop offset="1" stop-color="#f7f7f7"/>
      </linearGradient>
      <linearGradient id="footerTone" x1="0" y1="0" x2="0" y2="1">
        <stop offset="0" stop-color="#4a4a4a"/><stop offset="1" stop-color="#111111"/>
      </linearGradient>
    </defs>
    <rect class="photo-area" x="0" y="0" width="513" height="720" fill="url(#photoTone)" role="img" aria-label="Black and white photograph of stacked, curled legal papers on a desk"/>
    <path class="header-sweep" d="M165,0 C205,170 370,225 513,248 V0 Z" fill="url(#redSweep)"/>
    <path class="header-panel" d="M175,0 C220,150 370,200 513,220 V0 Z" fill="#ffffff"/>
    <path class="mid-sweep" d="M240,478 C380,480 480,560 513,610 V700 C470,600 380,505 240,492 Z" fill="url(#redSweep)"/>
    <path class="lower-panel" d="M0,480 H240 C370,500 465,590 513,690 V1080 H0 Z" fill="url(#lowerTone)" role="img" aria-label="Faint photograph of a handshake behind the text"/>
    <path class="footer-panel" d="M0,975 C160,935 380,930 513,965 V1080 H0 Z" fill="url(#footerTone)"/>
    <path class="footer-line" d="M0,972 C160,932 380,927 513,962" fill="none" stroke="#ffffff" stroke-width="2"/>
  </svg>

  <div class="brand">
    <div class="brand-name">PRESTWICKS</div>
    <div class="brand-sub">SOLICITORS</div>
  </div>

  <section class="practice-areas">
    <h2 class="practice-title">OUR AREAS OF <span class="accent">PRACTICE</span></h2>
    <ul class="practice-list">
      <li>Property Law</li>
      <li>Conveyancing</li>
      <li>Leases</li>
      <li>Criminal Law</li>
      <li>Family Law</li>
      <li>Litigation and Dispute Resolution</li>
      <li>Company Law</li>
      <li>Wills and Estates</li>
      <li>Powers of Attorney and Guardianship</li>
    </ul>
  </section>

  <div class="call-box">
    <div class="call-label">CALL TODAY</div>
    <div class="call-number">(02) 9418 3562</div>
  </div>

  <h2 class="section-tag">ABOUT US</h2>
  <div class="about-text">
    <p>Prestwicks is a Private Law Firm that has been servicing the Sydney area for over 35 years. With a dedicated, professional and friendly team we pride ourselves on delivering an exceptional legal service to our clients.</p>
    <p>We are passionate about our profession and committed to delivering results for our clients, so no matter what your legal enquiry is we are happy to listen.</p>
  </div>

  <div class="promise-banner">
    <div class="promise-line-1">ESTABLISHED FOR <span class="accent">OVER 35 YEARS</span></div>
    <div class="promise-line-2">YOU CAN FEEL CONFIDENT WITH OUR TEAM</div>
  </div>

  <ul class="contact-list">
    <li><svg viewBox="0 0 20 20"><circle cx="10" cy="10" r="9"/></svg>www.prestwickssolicitors-example.com.au</li>
    <li><svg viewBox="0 0 20 20"><path d="M10 1 L20 10 H17 V19 H12 V13 H8 V19 H3 V10 H0 Z"/></svg>3/82 Carradine Street, Liverpool, NSW 2170</li>
    <li><svg viewBox="0 0 20 20"><path d="M1 4 H19 V16 H1 Z M1 4 L10 11 L19 4" stroke="#111" stroke-width="1.2"/></svg>info@prestwickssolicitors-example.com.au</li>
  </ul>
</main>
</body>
</html>
```